Architectural Design Brochure

I need you to design 5 pages (they will be used as templates which I can then edit later).

Please design 5 pages - copy the example pdf provided as reference (Morrow Fold). Please copy pages 1,3,5,6,7 from the example provided. But make the style match my unique brand. I want the layout to be similar to the example but still must be unique - use my logo and brand style blue, white, silver and grey.

I must be able to edit the brochure myself after you have finished these 5 pages (to change text and images etc) so it must be given to me in suitable format which I can edit in (psd or gimp).

my website is www.plenwick.com.au
my logo is attached

Target Market(s)

Home Builders and Architects

Requirements
Must have
• I would like you to design it around my brand - white, blue, grey and silver.

Must do 5 pages, copy the layout as shown in the example Morrow Fold pdf - I need pages 1,3,5,6,7
Nice to have
• Unique stlye
same layout as example - pages 1,3,5,6,7
Should not have
• Should not be exactly same style / watermarks etc as example

```html
<!DOCTYPE html>
<html lang="en">
<head>
<meta charset="utf-8">
<title>Plenwick – Brochure Page 7</title>
<link rel="stylesheet" href="https://fonts.googleapis.com/css2?family=Questrial&family=Mulish:wght@700;800&display=swap">
<style>
  :root {
    --brand-blue: #1f8fd6;
    --brand-blue-deep: #0f6fb8;
    --text-grey: #8a8f96;
    --silver: #d7dbe0;
    --silver-light: #eceef1;
    --white: #ffffff;
  }
  * { margin: 0; padding: 0; box-sizing: border-box; }
  html, body { width: 841px; height: 1200px; overflow: hidden; background: var(--white); }
  .page {
    position: relative;
    width: 841px;
    height: 1200px;
    overflow: hidden;
    background: var(--white);
    font-family: "Questrial", sans-serif;
  }
  .intro-panel {
    position: absolute;
    left: 0; top: 0;
    width: 395px; height: 600px;
    background: var(--brand-blue);
    color: var(--white);
    padding: 34px 24px 0 30px;
    font-size: 16px;
    line-height: 1.24;
    z-index: 2;
  }
  .about-column {
    position: absolute;
    left: 436px; top: 130px;
    width: 378px;
    color: var(--brand-blue);
    font-size: 16px;
    line-height: 1.3;
  }
  .plan-drawing {
    position: absolute;
    left: 0; top: 580px;
    width: 372px; height: 262px;
    background: linear-gradient(160deg, var(--silver-light), #dfe2e6);
  }
  .building-photos {
    position: absolute;
    left: 392px; top: 545px;
    width: 449px; height: 297px;
    display: flex;
    gap: 4px;
  }
  .building-photos .photo { height: 100%; }
  .photo-one { flex: 1.1; background: linear-gradient(180deg, #c9dced, #b7bfc8 70%, #8f9a86); }
  .photo-two { flex: 1.3; background: linear-gradient(180deg, #b8d3ea, #e4e6e8 55%, #9aa08f); }
  .photo-three { flex: 1; background: linear-gradient(180deg, #c6dbee, #d9d6cf 60%, #a5a994); }
  .page-number {
    position: absolute;
    left: 24px; top: 905px;
    font-family: "Mulish", sans-serif;
    font-weight: 800;
    font-size: 230px;
    line-height: 1;
    color: var(--brand-blue);
    letter-spacing: -6px;
  }
  .states {
    position: absolute;
    left: 364px; top: 880px;
    width: 450px;
  }
  .states-heading {
    font-family: "Mulish", sans-serif;
    font-weight: 700;
    font-size: 25px;
    color: var(--brand-blue);
    margin-bottom: 14px;
  }
  .state-list {
    list-style: none;
    display: grid;
    grid-template-columns: 235px 1fr;
    row-gap: 6px;
    color: var(--text-grey);
    font-size: 15px;
  }
  .brand-mark {
    position: absolute;
    left: 598px; top: 1020px;
    display: flex;
    align-items: center;
    gap: 8px;
  }
  .brand-mark .dot {
    width: 20px; height: 20px;
    border-radius: 50%;
    background: var(--brand-blue);
  }
  .brand-mark .name {
    font-family: "Questrial", sans-serif;
    font-size: 24px;
    color: var(--brand-blue);
  }
  .footer-swoosh {
    position: absolute;
    left: 0; bottom: 0;
    width: 841px; height: 110px;
  }
  .tagline {
    position: absolute;
    right: 26px; bottom: 18px;
    font-family: "Questrial", sans-serif;
    font-style: italic;
    font-size: 20px;
    color: var(--white);
  }
</style>
</head>
<body>
<main class="page">
  <section class="intro-panel">
    <p>We are proud of our 7 business days policy and guarantee you exceptional communication and results customised to you. The high demand for our expertise is proof of our professionalism and efficiency of our design and drafting processes. Even within this timeframe, which is outstanding by industry standards' Morrow Fold Australia still ensures all jobs go through their twice checked policy (once by the drafter / designer then secondly by one of our drafting managers).</p>
    <p>Managing Directors, Graham Kellet and Maree Kellet started Morrow Fold Australia as a design and drafting firm who wanted to do things a bit different. They grew it by focusing on the fastest possible turnaround, with twice checked plans. Since then we have added 3D presentation services (both internal and external) and Commercial, Multi-Residential &amp; Industrial Design &amp; Documentation.</p>
  </section>

  <section class="about-column">
    <p>Our office is based in Brisbane and with the rapid growth, there are plans to expand into other states. The company was established over five years ago by Graham Kellet and Maree Kellet. They have over 15 years' experience in the industry and strive to ensure the best possible services to all builders, architects / designers and property developers Australia-wide. We take pride in the services we provide and we ensure our staff are always held in high regard within our workplace. We also have minimum drafting standards that we require staff to possess to be employed in our company.</p>
  </section>

  <div class="plan-drawing" role="img" aria-label="Architectural floor plan drawing of a residential layout"></div>

  <div class="building-photos">
    <div class="photo photo-one" role="img" aria-label="3D render of a multi-storey apartment building"></div>
    <div class="photo photo-two" role="img" aria-label="3D render of a modern residential complex with balconies"></div>
    <div class="photo photo-three" role="img" aria-label="3D render of townhouses with landscaping"></div>
  </div>

  <div class="page-number">7.</div>

  <section class="states">
    <h2 class="states-heading">We service clients in every state:</h2>
    <ul class="state-list">
      <li>Victoria</li><li>Tasmania</li>
      <li>New South Wales</li><li>Northern Territory</li>
      <li>Queensland</li><li>Australian Capital Territory</li>
      <li>Western Australia</li><li>South Australia</li>
    </ul>
  </section>

  <div class="brand-mark">
    <span class="dot"></span>
    <span class="name">Plenwick</span>
  </div>

  <svg class="footer-swoosh" viewBox="0 0 841 110" preserveAspectRatio="none" aria-hidden="true">
    <path d="M0 100 C 260 96, 520 70, 841 8 L841 110 L0 110 Z" fill="var(--silver)"/>
    <path d="M0 106 C 280 102, 540 80, 841 24 L841 110 L0 110 Z" fill="var(--brand-blue)"/>
  </svg>
  <p class="tagline">Clear plans. Careful detail. On time!</p>
</main>
</body>
</html>
```